We need a logo design that explain all the products we possess.
The main goal is to represent graphically all the logos, pointing to one single logo - Voltane.
The descriptions are in french.
I have uploaded a file with 4 logos to use:
Voltane (the logo that all the rest should be pointing to)
RDM
Parcelin
PattouMou
All logo must be used in the vector graphic format, the description file is in each folder, it's the description that should be next to the logo.

The main goal of this is to create a banner 10' x 11' (estimated)

Target Market(s)

Cities

Requirements
Must have
• All the logos in the zip file in vector graphic.
Nice to have
• A background
Should not have
• Do not use TOB logo, it's a mix with RDM, and Tob Blue/dark blue with inscription "RDM", Charging fees for a part of the picture is not ok!

```html
<!DOCTYPE html>
<html lang="fr">
<head>
<meta charset="utf-8">
<title>Portail Voltane 2.0</title>
<link rel="stylesheet" href="https://fonts.googleapis.com/css2?family=Roboto:wght@500;700;900&display=swap">
<style>
  :root {
    --bg-left: #a6c6d2;
    --bg-right: #8fd6ec;
    --disc-light: #ffffff;
    --disc-shade: #e6e9ec;
    --ink: #111111;
    --brand-blue: #1f6fb6;
    --pet-blue: #2aa5de;
    --parcel-blue: #2b5f9e;
    --arrow-red: #e5202b;
    --arrow-blue: #2a7fc4;
    --arrow-sky: #5cc6e6;
  }
  * { margin: 0; padding: 0; box-sizing: border-box; }
  html, body { width: 1200px; height: 1000px; overflow: hidden; }
  body { font-family: "Roboto", Arial, sans-serif; }
  .canvas {
    position: relative;
    width: 1200px;
    height: 1000px;
    overflow: hidden;
    background: linear-gradient(115deg, var(--bg-left) 0%, #a3cbd9 45%, var(--bg-right) 100%);
  }
  .arrows { position: absolute; inset: 0; }
  .disc {
    position: absolute;
    border-radius: 50%;
    background: radial-gradient(circle at 40% 35%, var(--disc-light) 55%, var(--disc-shade) 100%);
    border: 6px solid #ffffff;
    box-shadow: 18px 28px 40px rgba(40, 70, 90, 0.28);
    display: flex;
    flex-direction: column;
    align-items: center;
    text-align: center;
  }
  .disc--main { width: 572px; height: 572px; left: 314px; top: -70px; }
  .disc--pets { width: 304px; height: 304px; left: 58px; top: 538px; }
  .disc--council { width: 308px; height: 308px; left: 446px; top: 632px; }
  .disc--parcel { width: 312px; height: 312px; left: 816px; top: 528px; }

  .brand { font-weight: 900; line-height: 1; }
  .brand--main {
    margin-top: 310px;
    font-size: 64px;
    letter-spacing: 4px;
    color: var(--brand-blue);
  }
  .brand-mark {
    width: 18px; height: 18px; border-radius: 50%;
    background: var(--brand-blue);
    margin-top: 210px;
    position: absolute;
  }
  .caption { font-weight: 700; color: var(--ink); }
  .caption--main { margin-top: 36px; font-size: 22px; }

  .brand--pets { margin-top: 118px; font-size: 40px; color: var(--pet-blue); }
  .caption--pets { margin-top: 44px; font-size: 16px; }

  .brand--council { margin-top: 104px; font-size: 46px; color: var(--brand-blue); letter-spacing: 2px; }
  .caption--council { margin-top: 34px; font-size: 16px; }

  .brand--parcel { margin-top: 84px; font-size: 30px; font-weight: 500; letter-spacing: 5px; color: var(--parcel-blue); }
  .service-list {
    margin-top: 28px;
    list-style: none;
    text-align: left;
    font-weight: 700;
    font-size: 17px;
    line-height: 22px;
    color: var(--ink);
  }
  .service-list li::before {
    content: "";
    display: inline-block;
    width: 7px; height: 7px;
    border-radius: 50%;
    background: var(--ink);
    margin-right: 10px;
    vertical-align: middle;
  }
</style>
</head>
<body>
<main class="canvas">
  <svg class="arrows" width="1200" height="1000" viewBox="0 0 1200 1000" aria-hidden="true">
    <polygon points="244,512 344,456 344,572" fill="var(--arrow-red)"/>
    <polygon points="544,632 600,532 656,632" fill="var(--arrow-blue)"/>
    <polygon points="846,456 846,572 948,514" fill="var(--arrow-sky)"/>
  </svg>

  <section class="disc disc--main">
    <p class="brand brand--main">VOLTANE</p>
    <p class="caption caption--main">Portail Voltane 2.0</p>
  </section>

  <section class="disc disc--pets">
    <p class="brand brand--pets">PattouMou</p>
    <p class="caption caption--pets">Licences pour animaux</p>
  </section>

  <section class="disc disc--council">
    <p class="brand brand--council">RDM</p>
    <p class="caption caption--council">Conseil sans papier</p>
  </section>

  <section class="disc disc--parcel">
    <p class="brand brand--parcel">PARCELIN</p>
    <ul class="service-list">
      <li>Permis</li>
      <li>Carte</li>
      <li>Inventaire</li>
      <li>Taxes</li>
    </ul>
  </section>
</main>
</body>
</html>
```